Menu Board For a Bubble Tea Trailer

Berrisip is a bubble tea trailer that will be located in town and by the beach. Our aim is to bring refreshing beverages to our local community. My menu needs to reflect a bubbly and happy atmosphere of delicious fruit and some floral drinks, without looking unprofessional or childish.

My menu needs to be 1600mm long by 500mm high. It will be printed and attached to a sneeze guard for my beverage trailer which will be displayed on my serving window.

All drinks are priced as follows:
Regular: $6.50 Large: $7.50
Extra Topping: $0.60

Target Market(s)

Ages 15-39 including high school students, and young to middle aged workers that feel they need an energy or mood boost.

Industry/Entity Type

Bubble Tea (Non Alcoholic beverage)

Font styles to use
Sans Serif
Script

Colors
0094D4
00A9DD
6FCCEA
C7EBF8
E9F6FB
00AB8E
00BBA5
67D7C9
C6EFE9
E9F9F6
EE7325
F08F49
F5BC92
FAE3D3
FDF4ED
EB3D1F
EC4F4E
F09395
F8D3D4
FCEDEE

Requirements
Must have
• Pictures of bubble tea, Not crowded, easy to read, complimentary colours, prices, pictures must be in round bottom cups and without lid (attached)
Nice to have
• Bubbles or wave pattern
Should not have
• No black background, no fruits, no cartoon looking pictures

```html
<!DOCTYPE html>
<html lang="en">
<head>
<meta charset="UTF-8">
<title>Bubble Tea Menu Board</title>
<link rel="stylesheet" href="https://fonts.googleapis.com/css2?family=Pacifico&family=Quicksand:wght@500;600;700&display=block">
<style>
  :root {
    --ink: #3a2f33;
    --banner: #2f2529;
    --coral: #e8706c;
    --coral-soft: #f09395;
    --teal: #1bb8ae;
    --teal-deep: #00bba5;
    --wave-1: #e9f6f4;
    --wave-2: #d9efec;
    --wave-3: #c6e6e3;
    --divider: #e8dcc0;
    --white: #ffffff;
  }
  * { margin: 0; padding: 0; box-sizing: border-box; }
  html, body { width: 1200px; height: 375px; overflow: hidden; background: var(--white); }
  .menu-board {
    position: relative;
    width: 1200px;
    height: 375px;
    overflow: hidden;
    font-family: "Quicksand", sans-serif;
    color: var(--ink);
  }
  .backdrop { position: absolute; inset: 0; }

  .title-banner { position: absolute; left: 0; top: 0; width: 270px; height: 135px; }
  .title-top {
    position: absolute; left: 39px; top: 34px;
    font-family: "Quicksand", sans-serif; font-weight: 700;
    font-size: 22px; line-height: 24px; letter-spacing: 3.4px; color: var(--white);
    white-space: nowrap;
  }
  .title-script {
    position: absolute; left: 24px; top: 58px;
    font-family: "Pacifico", "Brush Script MT", cursive; font-size: 50px;
    line-height: 54px; height: 54px;
    color: var(--white); transform: rotate(-4deg); transform-origin: left center;
    white-space: nowrap;
  }

  .price-bar {
    position: absolute; left: 291px; top: 42px;
    display: flex; align-items: center;
    font-weight: 700; font-size: 22.5px; line-height: 28px; white-space: nowrap;
  }
  .price-bar .price { color: var(--coral); }
  .price-bar .sep {
    display: inline-block; width: 2px; height: 22px;
    background: var(--divider); margin: 0 17px;
  }

  .section { position: absolute; top: 96px; }
  .section-title {
    font-weight: 700; font-size: 24.5px; letter-spacing: 0.6px;
    line-height: 1; padding-bottom: 8px; white-space: nowrap;
  }
  .section-rule { height: 3px; border-radius: 2px; background: var(--teal); }
  .section-rule.coral { background: var(--coral); }
  .milk-tea { left: 291px; width: 238px; }
  .fruit-tea { left: 597px; width: 255px; }
  .toppings { left: 908px; width: 259px; }

  .item-list { position: absolute; top: 149px; list-style: none; }
  .item-list li { font-weight: 500; font-size: 15.5px; height: 27.5px; line-height: 20px; white-space: nowrap; }
  .item-list .sub-head { color: var(--teal); font-weight: 700; font-size: 15px; letter-spacing: 0.3px; }
  .col-milk-a { left: 291px; }
  .col-milk-b { left: 446px; }
  .col-fruit-a { left: 597px; }
  .col-fruit-b { left: 742px; }
  .col-top-a { left: 908px; }
  .col-top-b { left: 1036px; }

  .drink-art { position: absolute; }
  .drink-art.left-cups {
    left: 0; top: 170px; width: 240px; height: 185px;
    border-radius: 40px 40px 12px 12px;
    background: linear-gradient(90deg, #4f9a4a 0%, #b98ac8 30%, #efe4ea 50%, #c48a55 75%, #3b2c2a 100%);
    opacity: 0.9;
  }
  .drink-art.bottom-cups {
    left: 595px; top: 308px; width: 235px; height: 67px;
    border-radius: 30px 30px 0 0;
    background: linear-gradient(90deg, #e9706c 0%, #d9585a 45%, #7e4a78 60%, #5a3158 100%);
    opacity: 0.9;
  }
</style>
</head>
<body>
<main class="menu-board">
  <svg class="backdrop" width="1200" height="375" viewBox="0 0 1200 375" aria-hidden="true">
    <path d="M0 230 C180 180 320 130 470 150 C620 170 700 230 830 215 C960 200 1060 150 1200 160 L1200 375 L0 375 Z" fill="var(--wave-1)"/>
    <path d="M0 280 C200 250 340 220 520 250 C700 280 800 300 950 260 C1060 230 1130 240 1200 250 L1200 375 L0 375 Z" fill="var(--wave-2)"/>
    <path d="M0 320 C220 300 420 280 620 310 C820 340 980 300 1200 300 L1200 375 L0 375 Z" fill="var(--wave-3)"/>
    <path d="M860 215 C850 290 880 340 930 375" stroke="var(--white)" stroke-width="2" fill="none" opacity="0.8"/>
    <path d="M1085 150 C1100 190 1140 205 1200 200" stroke="var(--white)" stroke-width="2" fill="none" opacity="0.8"/>
    <path d="M1040 0 C1060 40 1100 75 1160 85 C1180 88 1200 90 1200 90 L1200 0 Z" fill="var(--coral)" opacity="0.9"/>
    <path d="M1180 0 C1175 40 1150 55 1148 80 C1146 105 1175 118 1200 122 L1200 0 Z" fill="var(--teal-deep)"/>
    <path d="M1200 0 L1185 0 C1187 15 1194 25 1200 28 Z" fill="#8fd2c8"/>
    <path d="M1200 235 C1185 235 1178 245 1180 255 C1182 265 1192 268 1200 265 Z" fill="var(--coral-soft)" opacity="0.9"/>
    <path d="M0 310 C60 300 120 310 170 330 C220 350 250 365 270 375 L0 375 Z" fill="var(--teal)"/>
    <path d="M30 180 C60 155 100 160 120 175 L30 200 Z" fill="var(--coral)"/>
    <circle cx="1186" cy="343" r="5" fill="var(--white)"/>
    <circle cx="1157" cy="329" r="5.5" fill="var(--white)"/>
    <circle cx="1188" cy="286" r="3" fill="var(--white)"/>
    <circle cx="1141" cy="361" r="3" fill="var(--white)"/>
  </svg>

  <div class="drink-art left-cups" role="img" aria-label="Watercolour bubble tea cups: green matcha, purple taro and brown milk tea with tapioca pearls and grass jelly"></div>
  <div class="drink-art bottom-cups" role="img" aria-label="Watercolour iced red fruit tea and purple taro slush"></div>

  <header class="title-banner">
    <svg width="270" height="135" viewBox="0 0 270 135" aria-hidden="true">
      <path d="M0 17 L262 17 L235 74 L266 131 L0 127 Z" fill="var(--banner)"/>
    </svg>
    <div class="title-top">BUBBLE TEA</div>
    <div class="title-script">Menu</div>
  </header>

  <div class="price-bar">
    <span>Regular:&nbsp;<span class="price">$6.50</span></span>
    <span class="sep"></span>
    <span>Large:&nbsp;<span class="price">$7.50</span></span>
    <span class="sep"></span>
    <span>Toppings:&nbsp;<span class="price">$0.60</span></span>
  </div>

  <section class="section milk-tea">
    <h2 class="section-title">MILK TEA</h2>
    <div class="section-rule"></div>
  </section>
  <ul class="item-list col-milk-a">
    <li>Thai</li><li>Royal</li><li>Original</li><li>Tiger Pearl</li><li>Young Coconut</li><li>Watermelon</li><li>Banana</li>
  </ul>
  <ul class="item-list col-milk-b">
    <li>Taro</li><li>Lychee</li><li>Honeydew</li><li>Strawberry</li><li>Lavender</li><li>Mango</li><li>Rose</li>
  </ul>

  <section class="section fruit-tea">
    <h2 class="section-title">GREEN TEA/RED TEA</h2>
    <div class="section-rule"></div>
  </section>
  <ul class="item-list col-fruit-a">
    <li>Peach</li><li>Mango</li><li>Passionfruit</li><li>Watermelon</li><li>Dragonfruit</li>
  </ul>
  <ul class="item-list col-fruit-b">
    <li>Grape</li><li>Lychee</li><li>Strawberry</li><li>Green Apple</li><li>Pomegranate</li>
  </ul>

  <section class="section toppings">
    <h2 class="section-title">TOPPINGS</h2>
    <div class="section-rule coral"></div>
  </section>
  <ul class="item-list col-top-a">
    <li class="sub-head">FRUIT JELLY</li><li>Rainbow</li><li>Lychee</li><li>Mango</li><li>Peach</li><li>Grape</li>
  </ul>
  <ul class="item-list col-top-b">
    <li class="sub-head">POPPING PEARLS</li><li>Peach</li><li>Mango</li><li>Lychee</li><li>Strawberry</li><li>Passionfruit</li><li>Watermelon</li>
  </ul>
</main>
</body>
</html>
```